Business Card & Logo Design Project

I am looking for a slick/simple design for a logo and business card, for a music Producer/Mixer/Engineer.

I'm based in Tokyo, Japan and I help my clients polish up their creation to major radio/TV status. My clients pay me for my taste, sense of balance expertise and creative direction/

Design should give impression of seal of quality, professionalism, and enthusiasm need some sort of a logo like design for "vantrix productions".

Please don't include music notes or instruments or anything musically related and anything samurai or ninja or too much Japan in them on the design.

I like clever, slick stuff that's not too obvious.
I also like a smooth gradation type transition. My favorite color is deep dark blue/

Good Luck and Thank you for your effort.
Updates

I would like a two-sided design for this one.
One side with "vantrix productions" (all lower case) on, and the other side with my name and contact info.

Please also consider portrait position (or direction).  (as opposed to landscape) 

Target Market(s)

My primary targets are artists & bands, who want absolute best for their creation.

Industry/Entity Type

Business

Requirements
Must have
• Two-Sided
1, vantrix productions
2, Kenji Harumoto, Producer/Mixer/Engineer, +81 090 4827 3516, brambleway@mailnest.example
Nice to have
• Any suggestions are welcome//
Should not have
• Anything music related images.
(e.g. CD, music notations, instruments etc.)

```html
<!DOCTYPE html>
<html lang="en">
<head>
<meta charset="utf-8">
<title>vantrix productions – business card</title>
<link rel="stylesheet" href="https://fonts.googleapis.com/css2?family=Exo+2:wght@500;600;700&display=swap">
<style>
  :root {
    --backdrop: #262626;
    --backdrop-edge: #141414;
    --card-light: #fafafa;
    --card-mid: #d9d9d9;
    --brand-blue: #1f5fb0;
    --deep-blue: #1a3f86;
    --accent-blue: #3a8fd9;
    --rule-blue: #6fa9e0;
    --pattern-light: #ececec;
    --pattern-dark: #d4d4d4;
  }
  * { box-sizing: border-box; margin: 0; padding: 0; }
  html, body {
    width: 1200px;
    height: 900px;
    overflow: hidden;
  }
  body {
    position: relative;
    background: radial-gradient(ellipse at 55% 40%, var(--backdrop) 0%, var(--backdrop-edge) 100%);
    font-family: "Exo 2", sans-serif;
  }
  .card {
    position: absolute;
    width: 520px;
    height: 300px;
    background: radial-gradient(ellipse at 50% 45%, var(--card-light) 0%, var(--card-mid) 100%);
    box-shadow: 0 12px 30px rgba(0, 0, 0, 0.6);
  }

  /* Back side: name and contact */
  .card-contact {
    left: 110px;
    top: 120px;
  }
  .card-contact .wordmark {
    position: absolute;
    left: 40px;
    top: 160px;
    font-size: 30px;
    font-weight: 700;
    color: var(--brand-blue);
    line-height: 1;
  }
  .contact-block {
    position: absolute;
    left: 290px;
    top: 78px;
  }
  .contact-group {
    border-left: 2px solid var(--rule-blue);
    padding-left: 10px;
    margin-bottom: 14px;
  }
  .person-name {
    font-size: 21px;
    font-weight: 700;
    color: var(--brand-blue);
    line-height: 1.1;
  }
  .person-role {
    font-size: 12px;
    font-weight: 600;
    color: var(--deep-blue);
  }
  .contact-line {
    font-size: 12px;
    font-weight: 500;
    color: var(--brand-blue);
    line-height: 1.45;
  }

  /* Front side: brand */
  .card-brand {
    left: 570px;
    top: 470px;
    overflow: hidden;
  }
  .brand-pattern {
    position: absolute;
    inset: 0;
    background: linear-gradient(135deg, var(--pattern-light) 0%, var(--pattern-dark) 50%, var(--pattern-light) 100%);
    opacity: 0.7;
  }
  .brand-lockup {
    position: absolute;
    inset: 0;
    display: flex;
    flex-direction: column;
    align-items: center;
    justify-content: center;
    gap: 26px;
  }
  .card-brand .wordmark {
    font-size: 50px;
    font-weight: 700;
    color: var(--brand-blue);
    line-height: 1;
  }
  .role-list {
    display: flex;
    align-items: center;
    gap: 10px;
    font-size: 18px;
    font-weight: 600;
    color: var(--deep-blue);
  }
  .role-divider {
    width: 2px;
    height: 14px;
    background: var(--accent-blue);
  }

  /* Standalone logo presentation */
  .logo-standalone {
    position: absolute;
    left: 48px;
    top: 805px;
    font-size: 30px;
    font-weight: 700;
    color: var(--accent-blue);
    line-height: 1;
  }
</style>
</head>
<body>

  <section class="card card-contact" aria-label="Business card, contact side">
    <div class="wordmark">vantrix productions</div>
    <div class="contact-block">
      <div class="contact-group">
        <div class="person-name">Kenji Harumoto</div>
        <div class="person-role">Producer/Mixer/Engineer</div>
      </div>
      <div class="contact-group">
        <div class="contact-line">P: +81 090 4827 3516</div>
        <div class="contact-line">E: brambleway@mailnest.example</div>
      </div>
    </div>
  </section>

  <section class="card card-brand" aria-label="Business card, brand side">
    <div class="brand-pattern" role="img" aria-label="Faint repeating brand-name background texture"></div>
    <div class="brand-lockup">
      <div class="wordmark">vantrix productions</div>
      <div class="role-list">
        <span>Producer</span>
        <span class="role-divider"></span>
        <span>Mixer</span>
        <span class="role-divider"></span>
        <span>Engineer</span>
      </div>
    </div>
  </section>

  <div class="logo-standalone">vantrix productions</div>

</body>
</html>
```